Toravel Project Consulting

I need a logo and business card design for a small business operating in the management consulting and contractor space, predominantly in local and state government. I specialise in project management, financial consulting, people and culture, procurement, ICT transformation and contracting for corporate support areas of organisations.

Industry/Entity Type

Business

```html
<!DOCTYPE html>
<html lang="en">
<head>
<meta charset="utf-8">
<title>Toravel Project Consulting – Business Card</title>
<link rel="stylesheet" href="https://fonts.googleapis.com/css2?family=Source+Sans+3:wght@400;600;700&display=swap">
<style>
  :root {
    --backdrop: #000000;
    --card: #333437;
    --card-edge: #2c2d30;
    --accent: #1673ea;
    --ink: #f2f2f2;
    --logo-grey: #9a9b9e;
    --divider: #3d3e42;
  }
  * { margin: 0; padding: 0; box-sizing: border-box; }
  html, body {
    width: 1200px;
    height: 900px;
    overflow: hidden;
    background: var(--backdrop);
    font-family: "Source Sans 3", "Myriad Pro", sans-serif;
  }
  .stage { position: relative; width: 1200px; height: 900px; }

  .card {
    position: absolute;
    top: 271px;
    width: 457px;
    height: 281px;
    border-radius: 14px;
    background: radial-gradient(ellipse at 50% 40%, var(--card) 0%, var(--card-edge) 100%);
  }
  .card--front { left: 137px; }
  .card--back { left: 626px; }

  /* Front */
  .brand-mark {
    position: absolute;
    left: 30px;
    top: 100px;
    display: flex;
    align-items: center;
    gap: 10px;
    color: var(--accent);
    font-weight: 700;
    font-size: 44px;
    line-height: 1;
  }
  .brand-mark__square {
    width: 26px;
    height: 26px;
    background: var(--accent);
  }
  .front-divider {
    position: absolute;
    left: 222px;
    top: 80px;
    width: 1px;
    height: 120px;
    background: var(--divider);
  }
  .contact {
    position: absolute;
    left: 259px;
    top: 59px;
    color: var(--ink);
    font-size: 13px;
    line-height: 19px;
  }
  .contact__name {
    color: var(--accent);
    font-size: 18px;
    font-weight: 700;
    line-height: 22px;
  }
  .contact__role { margin-bottom: 17px; }
  .contact__address { margin-bottom: 14px; }
  .contact__line { display: flex; align-items: center; gap: 5px; }
  .contact__icon { width: 9px; height: 9px; fill: var(--accent); }

  /* Back */
  .back-logo {
    position: absolute;
    left: 20px;
    top: 142px;
    width: 200px;
    text-align: center;
    color: var(--logo-grey);
    font-weight: 600;
    line-height: 1.05;
  }
  .back-logo__main { font-size: 28px; }
  .back-logo__sub { font-size: 13px; letter-spacing: 1px; text-transform: uppercase; margin-top: 4px; }

  .services {
    position: absolute;
    left: 232px;
    top: 47px;
    color: var(--ink);
  }
  .services__title {
    color: var(--accent);
    font-size: 17px;
    font-weight: 700;
    margin-bottom: 7px;
  }
  .services__list { list-style: none; font-size: 13px; font-weight: 600; }
  .services__item { position: relative; padding-left: 10px; line-height: 24px; }
  .services__item::before {
    content: "";
    position: absolute;
    left: 0;
    top: 10px;
    width: 5px;
    height: 5px;
    border-radius: 50%;
    background: var(--accent);
  }
  .services__item--continued::before { display: none; }
</style>
</head>
<body>
<main class="stage">
  <section class="card card--front">
    <div class="brand-mark">
      <span class="brand-mark__square"></span>
      <span>Toravel</span>
    </div>
    <div class="front-divider"></div>
    <div class="contact">
      <div class="contact__name">Liam Harper</div>
      <div class="contact__role">Director</div>
      <div class="contact__address">22 Wexcombe Parade<br>Northbridge NSW 2063</div>
      <div class="contact__line">
        <svg class="contact__icon" viewBox="0 0 10 10"><path d="M2 0.5 L3.6 0.5 L4.2 2.8 L3.1 3.6 Q4 5.6 6.3 6.9 L7.1 5.8 L9.5 6.4 L9.5 8 Q9.5 9.5 8 9.5 Q1 8.6 0.5 2 Q0.5 0.5 2 0.5 Z"/></svg>
        <span>0456123789</span>
      </div>
      <div class="contact__line">
        <svg class="contact__icon" viewBox="0 0 10 10"><path d="M0.5 2 H9.5 V8.5 H0.5 Z M0.5 2 L5 5.5 L9.5 2" fill="var(--accent)" stroke="var(--card)" stroke-width="0.8"/></svg>
        <span>info@toravelproject.com</span>
      </div>
      <div class="contact__line">
        <svg class="contact__icon" viewBox="0 0 10 10"><circle cx="5" cy="5" r="4.5"/><path d="M2.5 3 Q4 4 3.5 5.5 Q5 6 5 8 M6.5 1.8 Q6 3.5 7.8 4" stroke="var(--card)" stroke-width="0.8" fill="none"/></svg>
        <span>www.toravelproject.com</span>
      </div>
    </div>
  </section>

  <section class="card card--back">
    <div class="back-logo">
      <div class="back-logo__main">Toravel Project</div>
      <div class="back-logo__sub">Consulting</div>
    </div>
    <div class="services">
      <h2 class="services__title">Specialise in</h2>
      <ul class="services__list">
        <li class="services__item">Project management</li>
        <li class="services__item">Financial consulting</li>
        <li class="services__item">People and culture</li>
        <li class="services__item">Procurement</li>
        <li class="services__item">ICT transformation and</li>
        <li class="services__item">Contracting for corporate</li>
        <li class="services__item services__item--continued">support areas&nbsp; of organisations.</li>
      </ul>
    </div>
  </section>
</main>
</body>
</html>
```